We want a business card/punch card for our business. We are including examples of our current business card (we like the front of our business card and not looking to remake it). We need only back side to be designed in form of a punch card (we are including a sample of the punch card we made, but are unsatisfied). For each $180 spend (9 punches) our clients have $20 off.

Colors
886aae

```html
<!DOCTYPE html>
<html lang="en">
<head>
<meta charset="utf-8">
<title>Lumen Arts – Punch Card</title>
<link href="https://fonts.googleapis.com/css2?family=PT+Sans:wght@400;700&family=Fira+Sans+Condensed:wght@600;700&display=swap" rel="stylesheet">
<style>
  :root {
    --page-bg: #000000;
    --deep-purple: #5b2e91;
    --brand-purple: #886aae;
    --periwinkle: #5865b0;
    --lavender-light: #dfe3f5;
    --lavender-mid: #b9c1e6;
    --ink-purple: #4a3b96;
    --white: #ffffff;
  }
  * { box-sizing: border-box; margin: 0; padding: 0; }
  html, body {
    width: 1200px; height: 1000px; overflow: hidden;
    background: var(--page-bg);
  }
  .punch-card {
    position: absolute; left: 110px; top: 213px;
    width: 978px; height: 573px; overflow: hidden;
    background: var(--lavender-light);
  }
  .pattern-field {
    position: absolute; left: 240px; top: 0; width: 738px; height: 573px;
    background: radial-gradient(ellipse at 45% 40%, var(--lavender-light) 0%, var(--lavender-mid) 85%);
  }
  .card-shapes { position: absolute; inset: 0; }
  .brand {
    position: absolute; left: 30px; top: 40px; width: 190px;
    text-align: center; color: var(--white);
    font-family: "PT Sans", sans-serif;
  }
  .brand-dot {
    width: 86px; height: 86px; border-radius: 50%;
    background: var(--brand-purple); margin: 0 auto 22px;
  }
  .brand-name { font-size: 38px; font-weight: 400; line-height: 1; }
  .service-list {
    position: absolute; left: 33px; top: 260px;
    list-style: none; color: var(--white);
    font-family: "PT Sans", sans-serif; font-size: 27px; line-height: 41px;
  }
  .service-list li::before { content: "•"; margin-right: 6px; font-size: 20px; vertical-align: 3px; }
  .punch {
    position: absolute; width: 104px; height: 104px; border-radius: 50%;
    background: var(--white);
    box-shadow: 0 0 12px 6px rgba(255,255,255,0.7);
    display: flex; align-items: center; justify-content: center;
    font-family: "Fira Sans Condensed", sans-serif; font-weight: 600;
    font-size: 36px; color: var(--ink-purple);
  }
  .punch::before {
    content: ""; position: absolute; inset: 8px; border-radius: 50%;
    border: 6px double var(--periwinkle); opacity: 0.55;
  }
  .offer-band {
    position: absolute; left: 400px; top: 455px; width: 578px; height: 118px;
    background: var(--deep-purple); border-top: 4px solid var(--white);
    font-family: "Fira Sans Condensed", sans-serif; font-weight: 700; color: var(--white);
  }
  .offer-lead { position: absolute; left: 20px; top: 24px; font-size: 32px; }
  .offer-amount {
    position: absolute; left: 205px; top: -22px; font-size: 112px; line-height: 1;
    color: var(--periwinkle); -webkit-text-stroke: 3px var(--white); letter-spacing: -4px;
  }
  .offer-off {
    position: absolute; left: 278px; top: 14px; width: 58px; height: 58px; border-radius: 50%;
    background: var(--deep-purple); border: 3px solid var(--white);
    display: flex; align-items: center; justify-content: center; font-size: 26px;
  }
  .offer-tail { position: absolute; left: 360px; top: 14px; font-size: 38px; line-height: 38px; }
  .offer-rule { position: absolute; height: 0; border-top: 2px dotted var(--white); }
  .offer-rule.left { left: 20px; top: 72px; width: 185px; }
  .offer-rule.right { left: 448px; top: 34px; width: 72px; }
</style>
</head>
<body>
  <div class="punch-card">
    <div class="pattern-field" role="img" aria-label="Soft lavender mandala pattern background"></div>

    <svg class="card-shapes" width="978" height="573" viewBox="0 0 978 573" aria-hidden="true">
      <path d="M0 0 H300 C370 110 420 300 412 573 H0 Z" fill="#c8cdee"/>
      <path d="M0 0 H272 C345 120 400 300 404 573 H0 Z" fill="#8e9bd6"/>
      <path d="M0 0 H250 C325 120 385 300 392 573 H0 Z" fill="#5b2e91"/>
      <path d="M0 228 C160 220 300 255 350 320 C380 370 378 470 372 573 H0 Z" fill="#6f78c0"/>
      <path d="M0 240 C150 232 290 265 338 328 C366 375 364 470 358 573 H0 Z" fill="#5865b0"/>
    </svg>

    <div class="brand">
      <div class="brand-dot"></div>
      <div class="brand-name">Lumen Arts</div>
    </div>

    <ul class="service-list">
      <li>Tantra</li>
      <li>Sexual Healing</li>
      <li>Intimacy Coaching</li>
      <li>Sound Healing</li>
      <li>Sound Baths</li>
      <li>Crystal Healing</li>
      <li>Yoga</li>
    </ul>

    <div class="punch" style="left:474px;top:35px">$20</div>
    <div class="punch" style="left:624px;top:35px">$20</div>
    <div class="punch" style="left:772px;top:35px">$20</div>
    <div class="punch" style="left:474px;top:172px">$20</div>
    <div class="punch" style="left:624px;top:172px">$20</div>
    <div class="punch" style="left:772px;top:172px">$20</div>
    <div class="punch" style="left:474px;top:307px">$20</div>
    <div class="punch" style="left:624px;top:307px">$20</div>
    <div class="punch" style="left:772px;top:307px">$20</div>

    <div class="offer-band">
      <span class="offer-lead">9 Punches = $</span>
      <span class="offer-amount">20</span>
      <span class="offer-off">off</span>
      <span class="offer-tail">Your<br>Next Visit</span>
      <span class="offer-rule left"></span>
      <span class="offer-rule right"></span>
    </div>
  </div>
</body>
</html>
```